Velbrix SA

Découpe de métaux - Fourniture de tôles - Accessoires de machines de chantier (European Patent)

Les designs se ressemblent

Besoin de plus de jours pour examiner

• Mon projet doit comprendre la photo de la halle (bâtiment)

```html
<!DOCTYPE html>
<html lang="fr">
<head>
<meta charset="utf-8">
<title>Velbrix SA – Découpe de métaux</title>
<link href="https://fonts.googleapis.com/css2?family=Bebas+Neue&family=Oswald:wght@300&display=swap" rel="stylesheet">
<style>
  :root {
    --ink-dark: #252525;
    --paper: #ffffff;
    --text-light: #ffffff;
    --text-dark: #1f1f1f;
    --rule-grey: #c9c9c9;
    --grid-tint: rgba(255,255,255,0.03);
  }
  * { margin: 0; padding: 0; box-sizing: border-box; }
  html, body { width: 1200px; height: 866px; overflow: hidden; background: var(--paper); }
  .flyer { position: relative; width: 1200px; height: 866px; background: var(--paper); }
  .hero { position: absolute; left: 0; top: 0; width: 1200px; height: 757px; background: var(--ink-dark); }
  .grid-decor { position: absolute; background: var(--grid-tint); }
  .grid-decor--top { left: 880px; top: 12px; width: 310px; height: 250px; }
  .grid-decor--side { left: 16px; top: 300px; width: 300px; height: 440px; }
  .headline {
    position: absolute; left: 100px; top: 55px;
    font-family: "Bebas Neue", sans-serif; font-weight: 400;
    font-size: 198px; line-height: 184px; color: var(--text-light);
    letter-spacing: 1px;
  }
  .services {
    position: absolute; left: 94px; top: 482px;
    font-family: "Bebas Neue", sans-serif; font-size: 66px; line-height: 62px;
    color: var(--text-light); list-style: none;
  }
  .patent {
    position: absolute; left: 95px; top: 680px;
    font-family: "Oswald", sans-serif; font-weight: 300; font-size: 30px; line-height: 34px;
    color: var(--text-light); text-transform: uppercase; letter-spacing: -0.5px;
  }
  .hall-photo {
    position: absolute; left: 605px; top: 279px; width: 595px; height: 478px;
    background: linear-gradient(180deg, #5d80b3 0%, #4a5566 22%, #3a3e45 35%, #b7b8ba 48%, #a9a9a9 60%, #4d4b42 72%, #6f6a58 82%, #7a8a3a 100%);
  }
  .contact-bar {
    position: absolute; left: 0; top: 757px; width: 1200px; height: 109px;
    font-family: "Bebas Neue", sans-serif; font-size: 37px; color: var(--text-dark);
  }
  .contact-item { position: absolute; top: 22px; display: flex; align-items: center; }
  .contact-item::before {
    content: ""; display: block; width: 34px; height: 1px; background: var(--rule-grey);
    margin-right: 13px; margin-top: 20px;
  }
  .contact-item--email { left: 86px; }
  .contact-item--phone { left: 583px; }
  .contact-item--web { left: 870px; }
</style>
</head>
<body>
  <main class="flyer">
    <section class="hero">
      <div class="grid-decor grid-decor--top" role="img" aria-label="Grille décorative de petites croix"></div>
      <div class="grid-decor grid-decor--side" role="img" aria-label="Grille décorative de petites croix"></div>
      <h1 class="headline">Découpe de<br>métaux</h1>
      <ul class="services">
        <li>Fourniture de tôles</li>
        <li>Accessoires de</li>
        <li>machines de chantier</li>
      </ul>
      <p class="patent">(European patent)</p>
      <div class="hall-photo" role="img" aria-label="Photo de la halle Velbrix SA devant les montagnes, avec arbres et haie au premier plan"></div>
    </section>
    <footer class="contact-bar">
      <span class="contact-item contact-item--email">info@velbrix.ch</span>
      <span class="contact-item contact-item--phone">027/555.41.70</span>
      <span class="contact-item contact-item--web">www.velbrix.ch</span>
    </footer>
  </main>
</body>
</html>
```